Personal Injury Book Ad Photo Set

I need a series of images for a Pagebloom ad campaign for promoting a book titled "Making Sense of an Accident Claim".

```html
<!DOCTYPE html>
<html lang="en">
<head>
<meta charset="UTF-8">
<title>From Injury to Justice – Making Sense of an Accident Claim</title>
<link href="https://fonts.googleapis.com/css2?family=Poppins:wght@300;400;700;800&family=Montserrat:wght@500;600&display=swap" rel="stylesheet">
<style>
  :root {
    --ink: #262728;
    --accent: #d9860a;
    --bg-light: #f7f9fb;
    --bg-blue: #c7d9e5;
    --cover-top: #ffffff;
    --cover-bottom: #dfe8f0;
    --pages: #e9ecef;
    --pages-edge: #c9ced3;
  }
  * { box-sizing: border-box; margin: 0; padding: 0; }
  html, body { width: 1200px; height: 1200px; overflow: hidden; }
  body { font-family: "Poppins", sans-serif; }

  .ad {
    position: relative;
    width: 1200px;
    height: 1200px;
    background: linear-gradient(135deg, var(--bg-light) 0%, #e6eef4 50%, var(--bg-blue) 100%);
    color: var(--ink);
  }

  .headline {
    position: absolute;
    top: 104px;
    left: 0;
    width: 100%;
    text-align: center;
    line-height: 1;
  }
  .headline__line { display: block; white-space: nowrap; }
  .headline__line--second { margin-top: 20px; }
  .headline__small {
    font-family: "Poppins", sans-serif;
    font-size: 54px;
    font-weight: 300;
    color: var(--ink);
    margin-right: 10px;
  }
  .headline__big {
    font-family: "Poppins", sans-serif;
    font-weight: 800;
    letter-spacing: -2px;
  }
  .headline__big--first { font-size: 100px; color: var(--ink); }
  .headline__big--second { font-size: 122px; color: var(--accent); }

  .book {
    position: absolute;
    left: 423px;
    top: 394px;
    width: 314px;
    height: 492px;
    filter: drop-shadow(0 16px 18px rgba(40, 60, 80, 0.25));
  }
  .book__pages {
    position: absolute;
    right: 0;
    top: 10px;
    width: 24px;
    height: 480px;
    background: repeating-linear-gradient(90deg, var(--pages) 0 2px, var(--pages-edge) 2px 3px);
    border-radius: 0 3px 3px 0;
  }
  .book__cover {
    position: absolute;
    left: 0;
    top: 0;
    width: 292px;
    height: 492px;
    background: linear-gradient(180deg, var(--cover-top) 0%, #eef3f7 55%, var(--cover-bottom) 100%);
    border-radius: 2px 4px 4px 2px;
    overflow: hidden;
    text-align: center;
  }
  .book__spine-shade {
    position: absolute;
    left: 0; top: 0;
    width: 10px; height: 100%;
    background: linear-gradient(90deg, rgba(0,0,0,0.12), rgba(0,0,0,0));
  }
  .cover-title {
    position: absolute;
    top: 48px;
    left: 0;
    width: 100%;
    line-height: 1;
  }
  .cover-title__line { display: block; white-space: nowrap; }
  .cover-title__line--second { margin-top: 6px; }
  .cover-title__small {
    font-family: "Poppins", sans-serif;
    font-weight: 300;
    font-size: 18px;
    color: var(--ink);
    margin-right: 4px;
  }
  .cover-title__big {
    font-family: "Poppins", sans-serif;
    font-weight: 800;
    letter-spacing: -1px;
  }
  .cover-title__big--first { font-size: 38px; color: var(--ink); }
  .cover-title__big--second { font-size: 42px; color: var(--accent); }

  .cover-photo {
    position: absolute;
    top: 150px;
    left: 0;
    width: 100%;
    height: 180px;
    background:
      radial-gradient(ellipse 45% 40% at 50% 60%, rgba(60,40,30,0.55), rgba(60,40,30,0) 70%),
      linear-gradient(180deg, #f3f6f9 0%, #c9d7e3 55%, #e8eef3 100%);
  }

  .cover-subtitle {
    position: absolute;
    top: 340px;
    left: 0;
    width: 100%;
    font-family: "Montserrat", sans-serif;
    font-weight: 500;
    font-size: 14px;
    letter-spacing: 0.32em;
    line-height: 1.3;
    color: var(--ink);
  }
  .cover-subtitle .accent { color: var(--accent); font-weight: 600; }

  .cover-author {
    position: absolute;
    top: 432px;
    left: 0;
    width: 100%;
    font-family: "Montserrat", sans-serif;
    font-weight: 600;
    font-size: 21px;
    letter-spacing: 0.14em;
    color: var(--ink);
  }

  .tagline {
    position: absolute;
    top: 928px;
    left: 0;
    width: 100%;
    text-align: center;
    font-family: "Poppins", sans-serif;
    font-weight: 300;
    font-size: 44px;
    letter-spacing: 0.3em;
    line-height: 56px;
    color: #111;
    text-transform: uppercase;
  }
  .tagline__line { display: block; padding-left: 0.3em; }
  .tagline .accent { color: var(--accent); }
</style>
</head>
<body>
<main class="ad">
  <h1 class="headline">
    <span class="headline__line"><span class="headline__small">From</span><span class="headline__big headline__big--first">INJURY</span></span>
    <span class="headline__line headline__line--second"><span class="headline__small">to</span><span class="headline__big headline__big--second">JUSTICE</span></span>
  </h1>

  <div class="book" aria-label="Book: From Injury to Justice">
    <div class="book__pages"></div>
    <div class="book__cover">
      <div class="cover-title">
        <span class="cover-title__line"><span class="cover-title__small">From</span><span class="cover-title__big cover-title__big--first">INJURY</span></span>
        <span class="cover-title__line cover-title__line--second"><span class="cover-title__small">to</span><span class="cover-title__big cover-title__big--second">JUSTICE</span></span>
      </div>
      <div class="cover-photo" role="img" aria-label="Photo of a judge's gavel resting beside a stethoscope"></div>
      <div class="cover-subtitle">
        MAKING SENSE OF<br>AN <span class="accent">ACCIDENT</span><br>CLAIM
      </div>
      <div class="cover-author">AUTHOR NAME</div>
      <div class="book__spine-shade"></div>
    </div>
  </div>

  <p class="tagline">
    <span class="tagline__line">Making Sense of</span>
    <span class="tagline__line">An <span class="accent">Accident</span></span>
    <span class="tagline__line">Claim</span>
  </p>
</main>
</body>
</html>
```